Advertising flyer for proofreading business.

Hello everyone,

I need an advertising flyer for a new proofreading company in Australia.

I would like your design in be in two sizes:
- A4 (to be posted on noticeboards),
- A6 (to be printed in larger quantity to give away)
(please see the size specification file attached).

The text file is attached (Ad Text) and it contains lots of information. Please feel free to include your choice of text from the text file, but please include Poster title, and highlight 'ESL' and students discounts.

I understand that it is impossible to include the same amount of information on A6 and A4, so please feel free to chose what fits on each of them, but please keep the design similar.

I have attached our company logo, but feel free to adjust it to the poster design (feel free to change the color as well). The original logo file contains circle around it, please feel free to remove it and include only the typeset as it can be seen here: http://www.vellumcheck.com.au/.

Flyers will be printed, so please see the specification file for details.

I will do my best to respond to feedback as soon as possible.

I appreciate your participation, time and help,
Best wishes,
Radoslaw

Target Market(s)

Students, authors

Industry/Entity Type

Business

Colors

Designer to choose colors to be used in the design.

Requirements
Must have
• It would be good if poster is easy to spot on busy noticeboards and attract attention.
• Please keep the poster in the positive/optimistic mood, and so that it focuses on students, maybe photos of graduates(?).
• Poster title,
• Please include the list of proof-read documents as they are described in the attached text file (Ad Text).
• Please highlight students discounts and ESL.
Nice to have
• I would like to leave the creative freedom to all designers so at this point I have not adjusted the Look and Feel sliders. Please feel free to offer your own take on this.
• It would be nice if most of the text could be fit to the poster.

```html
<!DOCTYPE html>
<html lang="en">
<head>
<meta charset="utf-8">
<title>Vellumcheck proofreading flyers</title>
<link href="https://fonts.googleapis.com/css2?family=Exo+2:ital,wght@0,400;0,500;0,600;0,700;1,400&display=swap" rel="stylesheet">
<style>
:root{
  --teal:#2bb99a;
  --teal-soft:#5fcfb6;
  --teal-line:#8fe0cd;
  --ink:#3a3a3a;
  --muted:#6f6f6f;
  --frame:#9a9a9a;
  --paper:#ffffff;
}
*{box-sizing:border-box;margin:0;padding:0}
html,body{width:1200px;height:848px;overflow:hidden;background:var(--paper)}
body{position:relative;font-family:"Exo 2",sans-serif;color:var(--ink)}
.flyer{position:absolute;top:122px;width:428px;height:605px;border:1px solid var(--frame);background:var(--paper);overflow:hidden}
.flyer--desk{left:145px}
.flyer--writer{left:626px}
.brand-box{position:absolute;left:30px;top:30px;width:138px;height:52px;border:2px solid var(--teal);text-align:center;padding-top:8px}
.brand-name{color:var(--teal);font-weight:700;font-size:15px;letter-spacing:.5px;line-height:18px}
.brand-tag{color:var(--teal);font-weight:600;font-size:6.2px;margin-top:5px}
.doc-list{position:absolute;left:31px;top:95px;list-style:none}
.doc-list li{font-size:8px;line-height:15.8px;color:var(--muted);padding-left:13px;position:relative}
.chev::before,.doc-list li::before{content:"»";position:absolute;left:0;color:var(--teal);font-weight:700}
.turnaround{position:absolute;left:30px;top:366px;width:108px;height:30px;border:2px solid var(--teal);color:var(--teal);font-size:7.4px;font-weight:600;display:flex;align-items:center;padding-left:10px}
.same-day{position:absolute;left:30px;top:405px;font-size:8px;line-height:10.5px;color:var(--ink)}
.quote-call{position:absolute;left:30px;top:436px;font-size:8px;line-height:10.5px;color:var(--muted)}
.contacts{position:absolute;left:31px;top:468px;list-style:none}
.contacts li{position:relative;padding-left:13px;font-size:7.8px;line-height:10.4px;font-weight:500}
.contacts li::before{content:"»";position:absolute;left:0;color:var(--teal);font-weight:700}
.mark{position:absolute;left:30px;top:520px;width:48px;text-align:center}
.mark-dot{width:44px;height:44px;border-radius:50%;background:var(--teal);margin:0 auto}
.mark-name{color:var(--teal);font-size:7px;font-weight:600;margin-top:3px}
.photo{position:absolute;left:183px;top:0;width:245px;height:245px}
.flyer--desk .photo{background:linear-gradient(150deg,#f4f4f2 0%,#e9ebe8 45%,#d7d9d6 70%,#3a3d42 100%)}
.flyer--writer .photo{background:linear-gradient(160deg,#556478 0%,#7f8a98 35%,#c9b9a4 60%,#9aa4ae 80%,#2e3540 100%)}
.offer{position:absolute;left:183px;top:245px;width:245px;height:243px;background:var(--teal);color:#fff}
.price-box{position:absolute;left:201px;top:233px;width:196px;height:67px;border:2px solid var(--teal-line);padding:10px 0 0 13px;color:#fff;font-size:19px;font-weight:600;line-height:22px}
.price-box sup{font-size:8px}
.esl-badge{position:absolute;left:358px;top:264px;width:58px;height:58px;border-radius:50%;background:var(--teal-soft);color:#fff;font-size:8px;font-weight:600;display:flex;align-items:center;justify-content:center;text-align:center;line-height:10px}
.offer-copy{position:absolute;left:201px;top:312px;width:210px;font-size:7.2px;line-height:9.6px;color:#fff}
.offer-copy b{font-weight:700}
.offer-points{position:absolute;left:201px;top:360px;width:200px;list-style:none;color:#fff}
.offer-points li{position:relative;padding-left:13px;font-size:7.2px;line-height:9.4px;margin-bottom:4px}
.offer-points li::before{content:"»";position:absolute;left:0;font-weight:700}
.discount-box{position:absolute;left:201px;top:406px;width:196px;height:29px;border:2px solid var(--teal-line);color:#fff;font-size:7.4px;font-weight:600;display:flex;align-items:center;padding-left:11px}
.student-rate{position:absolute;left:201px;top:448px;width:210px;font-size:7.2px;line-height:9.4px;color:#fff}
.student-rate b{font-weight:700}
.package{position:absolute;left:201px;top:473px;font-size:7.2px;color:#fff}
.footnote{position:absolute;left:183px;top:492px;width:240px;font-size:5.4px;line-height:7px;font-style:italic;color:var(--muted)}
.testimonial{position:absolute;left:95px;top:518px;width:320px;height:56px}
.testimonial-bracket{position:absolute;left:0;top:0;width:30px;height:56px;border:3px solid var(--frame);border-right:none}
.testimonial-quote{position:absolute;left:13px;top:13px;width:300px;font-size:6.4px;line-height:10px;font-weight:600;color:var(--teal)}
.testimonial-by{position:absolute;left:13px;top:36px;font-size:5px;font-style:italic;color:var(--muted)}
.contact-bar{position:absolute;left:183px;top:584px;width:245px;height:21px;background:var(--teal);color:#fff;font-size:7px;font-weight:600;display:flex;align-items:center;justify-content:center}
</style>
</head>
<body>

<article class="flyer flyer--desk">
  <div class="brand-box"><div class="brand-name">‘VELLUMCHECK’</div><div class="brand-tag">Professional Proofreading Services</div></div>
  <ul class="doc-list"><li>essays</li><li>assignments</li><li>theses</li><li>resumes</li><li>business correspondence</li><li>training manuals</li><li>newsletters</li><li>advertising copy</li><li>brochures</li><li>catalogue</li><li>media releases</li><li>websites</li><li>presentations</li><li>speeches</li><li>novels</li><li>short stories</li></ul>
  <div class="turnaround">Fast turnaround times</div>
  <p class="same-day">Same day service can be<br>provided by special arrangement.</p>
  <p class="quote-call">Contact Harriet for an<br>obligation-free quote:</p>
  <ul class="contacts"><li>0400 555 218</li><li>proofing@vellumcheck.com.au</li></ul>
  <div class="mark"><div class="mark-dot"></div><div class="mark-name">vellumcheck</div></div>
  <div class="photo" role="img" aria-label="Photo of a white desk with a keyboard, potted plant, paper clips, reading glasses and a black notebook"></div>
  <div class="offer"></div>
  <div class="price-box">Prices start from<br>$20 per page<sup>*</sup></div>
  <div class="esl-badge">Help<br>with ESL</div>
  <p class="offer-copy">Professional , English-language proofreading:<br>Help with <b>English as a second language (ESL)</b><br>- native English speaker with English Honours<br>degree will correct all English language<br>errors, spelling and grammar mistakes.</p>
  <ul class="offer-points"><li>Includes referencing and editing for style,<br>coherence and clarity.</li><li>Fast, negotiable time-frames.</li></ul>
  <div class="discount-box">Student &amp; not-for-profit discount</div>
  <p class="student-rate"><b>Special student discount rate:</b> $25 per hour - roughly<br>1000 words (4 pages) of well-written text.</p>
  <p class="package">Package deals on documents over 50,000 words.</p>
  <p class="footnote">*Additional charges may apply for longer and/or more complex documents<br>(e.g. documents requiring specialist help with English as a second language).</p>
  <div class="testimonial"><div class="testimonial-bracket"></div><p class="testimonial-quote">“Harriet understood our requirements quickly and has been fantastic at delivering quality work, on time and within agreed budget. It’s a pleasure to work with her.”</p><p class="testimonial-by">Joan Whitby, Operations Manager, Corvane</p></div>
  <div class="contact-bar">0400 555 218 / proofing@vellumcheck.com.au</div>
</article>

<article class="flyer flyer--writer">
  <div class="brand-box"><div class="brand-name">‘VELLUMCHECK’</div><div class="brand-tag">Professional Proofreading Services</div></div>
  <ul class="doc-list"><li>essays</li><li>assignments</li><li>theses</li><li>resumes</li><li>business correspondence</li><li>training manuals</li><li>newsletters</li><li>advertising copy</li><li>brochures</li><li>catalogue</li><li>media releases</li><li>websites</li><li>presentations</li><li>speeches</li><li>novels</li><li>short stories</li></ul>
  <div class="turnaround">Fast turnaround times</div>
  <p class="same-day">Same day service can be<br>provided by special arrangement.</p>
  <p class="quote-call">Contact Harriet for an<br>obligation-free quote:</p>
  <ul class="contacts"><li>0400 555 218</li><li>proofing@vellumcheck.com.au</li></ul>
  <div class="mark"><div class="mark-dot"></div><div class="mark-name">vellumcheck</div></div>
  <div class="photo" role="img" aria-label="Photo of a hand marking printed pages with a pen beside a laptop keyboard"></div>
  <div class="offer"></div>
  <div class="price-box">Prices start from<br>$20 per page<sup>*</sup></div>
  <div class="esl-badge">Help<br>with ESL</div>
  <p class="offer-copy">Professional , English-language proofreading:<br>Help with <b>English as a second language (ESL)</b><br>- native English speaker with English Honours<br>degree will correct all English language<br>errors, spelling and grammar mistakes.</p>
  <ul class="offer-points"><li>Includes referencing and editing for style,<br>coherence and clarity.</li><li>Fast, negotiable time-frames.</li></ul>
  <div class="discount-box">Student &amp; not-for-profit discount</div>
  <p class="student-rate"><b>Special student discount rate:</b> $25 per hour - roughly<br>1000 words (4 pages) of well-written text.</p>
  <p class="package">Package deals on documents over 50,000 words.</p>
  <p class="footnote">*Additional charges may apply for longer and/or more complex documents<br>(e.g. documents requiring specialist help with English as a second language).</p>
  <div class="testimonial"><div class="testimonial-bracket"></div><p class="testimonial-quote">“Harriet understood our requirements quickly and has been fantastic at delivering quality work, on time and within agreed budget. It’s a pleasure to work with her.”</p><p class="testimonial-by">Joan Whitby, Operations Manager, Corvane</p></div>
  <div class="contact-bar">0400 555 218 / proofing@vellumcheck.com.au</div>
</article>

</body>
</html>
```